A label for my commercially sold local honey. This is a LABEL not a logo

3 inches high
2 inches wide

Target Market(s)

Customers who like "local" honey

Logo Text

Wildflower Honey -- 100% Pure & Unfiltered -- Florida

Logo styles of interest
Wordmark Logo
Requirements
Must have
• Wildflower Honey -- 100% Pure & Unfiltered -- Florida

Florida should be dominant

3 inches high / 2 inches wide

```html
<!DOCTYPE html>
<html lang="en">
<head>
<meta charset="utf-8">
<title>Wildflower Honey Label</title>
<link href="https://fonts.googleapis.com/css2?family=Jost:wght@400;700&display=swap" rel="stylesheet">
<style>
  :root {
    --paper: #ffffff;
    --label-fill: #f6d076;
    --label-rim: #8a1106;
    --ink: #2e201c;
    --hive-orange: #d15f05;
    --bee-black: #141414;
  }
  html, body {
    margin: 0;
    padding: 0;
    width: 1200px;
    height: 1000px;
    overflow: hidden;
    background: var(--paper);
  }
  .canvas {
    position: relative;
    width: 1200px;
    height: 1000px;
  }
  .label-shape {
    position: absolute;
    left: 0;
    top: 0;
  }
  .label-text {
    position: absolute;
    left: 0;
    width: 1200px;
    text-align: center;
    color: var(--ink);
    font-family: "Jost", "Futura", sans-serif;
    margin: 0;
    line-height: 1;
  }
  .title-top {
    top: 136px;
    font-size: 62px;
    font-weight: 700;
    letter-spacing: 0.5px;
  }
  .title-main {
    top: 196px;
    font-size: 108px;
    font-weight: 700;
    letter-spacing: 1px;
  }
  .emblem-art {
    position: absolute;
    left: 400px;
    top: 313px;
    width: 400px;
    height: 320px;
    border-radius: 24px;
    background: radial-gradient(circle at 50% 55%, var(--bee-black) 0%, #5a2c08 30%, var(--hive-orange) 55%, rgba(209, 95, 5, 0.35) 80%, rgba(246, 208, 118, 0) 100%);
  }
  .maker-name {
    top: 668px;
    font-size: 36px;
    font-weight: 700;
  }
  .region {
    top: 760px;
    font-size: 78px;
    font-weight: 700;
    letter-spacing: 1px;
  }
  .claim {
    top: 846px;
    font-size: 27px;
    font-weight: 400;
    letter-spacing: 3px;
    line-height: 31px;
  }
</style>
</head>
<body>
  <main class="canvas">
    <svg class="label-shape" width="1200" height="1000" viewBox="0 0 1200 1000" aria-hidden="true">
      <rect x="310" y="33" width="581" height="934" rx="168" ry="168" fill="var(--label-fill)" stroke="var(--label-rim)" stroke-width="7"/>
      <rect x="331" y="54" width="539" height="892" rx="148" ry="148" fill="none" stroke="var(--label-rim)" stroke-width="4.5"/>
    </svg>

    <h1 class="label-text title-top">WILDFLOWER</h1>
    <p class="label-text title-main">HONEY</p>

    <div class="emblem-art" role="img" aria-label="Illustration of a bumblebee on an orange honeycomb hexagon with three crossed honey dippers"></div>

    <p class="label-text maker-name">Palmetto Hive Co.</p>

    <p class="label-text region">FLORIDA</p>
    <p class="label-text claim">100% PURE<br>&amp; UNFILTERED</p>
  </main>
</body>
</html>
```